Patternmaking service (fashion) card design

I need cards for my patternmaking service. I service both large and small fashion labels including ladies,mens and childrenswear. I would like cards that have a sort of vintage feel, especially 50's and 60's style. Pink is my signature colour. Its important to have a fashion reference of some kind.

Industry/Entity Type

Fashion

Contact Information for Business Card

Marigold Thimble, Patternmaking Service, Kessa Vantorin,
27 Pellham Lane. Ashbrook Vale. VIC. 3152. 0415836204, email:lacebird4@mailnest.example. "By appointment only"

```html
<!DOCTYPE html>
<html lang="en">
<head>
<meta charset="utf-8">
<title>Marigold Thimble – Business Card</title>
<link rel="stylesheet" href="https://fonts.googleapis.com/css2?family=Gelasio:wght@400;700&family=Sorts+Mill+Goudy&display=swap">
<style>
  :root {
    --card-pink: #f9d6d7;
    --contact-red: #b1393d;
    --brand-maroon: #5c1b1e;
    --tagline-grey: #4a3536;
    --band-rose: #c7625f;
    --band-rose-soft: #e3a3a2;
    --ornament-rose: #cf7674;
  }
  * { margin: 0; padding: 0; box-sizing: border-box; }
  html, body { width: 1200px; height: 741px; overflow: hidden; background: var(--card-pink); }
  .card {
    position: relative;
    width: 1200px;
    height: 741px;
    background: var(--card-pink);
    font-family: "Gelasio", Georgia, serif;
    overflow: hidden;
  }
  .contact {
    position: absolute;
    left: 108px;
    top: 102px;
    color: var(--contact-red);
    font-style: normal;
    font-size: 26px;
    line-height: 37px;
  }
  .contact .name { font-weight: 700; font-size: 30px; line-height: 38px; }
  .appointment {
    position: absolute;
    left: 144px;
    top: 351px;
    color: var(--contact-red);
    font-size: 24px;
  }
  .ornament-area {
    position: absolute;
    left: 0;
    top: 492px;
    width: 1200px;
    height: 78px;
  }
  .rule-band {
    position: absolute;
    left: 0;
    top: 571px;
    width: 1200px;
    height: 13px;
    border-top: 3px solid var(--band-rose);
    border-bottom: 3px solid var(--band-rose);
    background: var(--band-rose-soft);
  }
  .brand {
    position: absolute;
    right: 119px;
    top: 586px;
    text-align: right;
    font-family: "Sorts Mill Goudy", Georgia, serif;
  }
  .brand .brand-name {
    color: var(--brand-maroon);
    font-size: 64px;
    line-height: 66px;
  }
  .brand .tagline {
    color: var(--tagline-grey);
    font-size: 31px;
    line-height: 30px;
  }
  .footer-band {
    position: absolute;
    left: 0;
    top: 689px;
    width: 1200px;
    height: 15px;
    background: var(--band-rose);
  }
</style>
</head>
<body>
  <main class="card">
    <address class="contact">
      <div class="name">Kessa Vantorin</div>
      <div>27 Pellham Lane</div>
      <div>Ashbrook Vale</div>
      <div>VIC. 3152</div>
      <div>0415836204</div>
      <div>email:lacebird4@mailnest.example</div>
    </address>
    <p class="appointment">"By appointment only"</p>

    <svg class="ornament-area" viewBox="0 0 1200 78" role="img" aria-label="Vintage scrollwork and floral flourish ornament in dusty rose">
      <defs>
        <linearGradient id="ornamentTone" x1="0" x2="1" y1="0" y2="0">
          <stop offset="0" stop-color="#cf7674" stop-opacity="0.15"/>
          <stop offset="0.15" stop-color="#cf7674" stop-opacity="0.6"/>
          <stop offset="1" stop-color="#cf7674" stop-opacity="0.7"/>
        </linearGradient>
      </defs>
      <rect x="0" y="0" width="1200" height="78" fill="url(#ornamentTone)"/>
    </svg>
    <div class="rule-band"></div>

    <div class="brand">
      <div class="brand-name">Marigold Thimble</div>
      <div class="tagline">Patternmaking Service</div>
    </div>

    <div class="footer-band"></div>
  </main>
</body>
</html>
```